Copperfinch Menu

I want to re design my menu at our restaurant Copperfinch, the current menu and information about the restaurant is online at www.copperfinch-eatery.example, have attached the logo for Copperfinch as well as the new menu specifications

Menu design Specifications
· Rustic

· Raw

· Unpolished

· Urban

```html
<!DOCTYPE html>
<html lang="en">
<head>
<meta charset="utf-8">
<title>Copperfinch Menu</title>
<link rel="stylesheet" href="https://fonts.googleapis.com/css2?family=Arimo:wght@400;700&family=Cormorant+Garamond:ital,wght@1,600&display=swap">
<style>
  :root {
    --wood-dark: #4a3526;
    --wood-mid: #7a5f4a;
    --wood-light: #9c8270;
    --panel: rgba(244, 241, 238, 0.9);
    --wine: #8b1a2a;
    --ink-blue: #0d4f9c;
  }
  * { margin: 0; padding: 0; box-sizing: border-box; }
  html, body { width: 887px; height: 1200px; overflow: hidden; }
  body {
    position: relative;
    font-family: "Arimo", Arial, sans-serif;
    color: var(--wine);
  }
  .wood-backdrop {
    position: absolute; inset: 0;
    background: linear-gradient(90deg, var(--wood-dark) 0%, var(--wood-mid) 20%, var(--wood-light) 50%, var(--wood-mid) 80%, var(--wood-dark) 100%);
  }
  .brand-panel {
    position: absolute; left: 35px; top: 23px; width: 814px; height: 162px;
    background: var(--panel);
    display: flex; align-items: center; justify-content: center;
  }
  .brand-name {
    font-family: "Arimo", Arial, sans-serif;
    font-weight: 700;
    font-size: 96px;
    letter-spacing: 4px;
    text-transform: uppercase;
    color: #221c19;
  }
  .menu-panel {
    position: absolute; left: 25px; top: 203px; width: 836px; height: 967px;
    background: var(--panel);
  }
  .section-title {
    position: absolute; left: 26px;
    font-family: "Cormorant Garamond", Georgia, serif;
    font-style: italic; font-weight: 600;
    font-size: 78px; line-height: 1;
    letter-spacing: 1.5px;
    color: var(--ink-blue);
  }
  .section-rule { position: absolute; left: 21px; width: 776px; height: 24px; }
  .item-list { position: absolute; left: 21px; list-style: none; }
  .item {
    display: flex; align-items: baseline;
    height: 35px; font-size: 20px; line-height: 35px;
  }
  .item-name { white-space: nowrap; }
  .leader {
    flex: 1; margin: 0 4px;
    border-bottom: 2px dotted var(--wine);
    transform: translateY(-5px);
  }
  .price { text-align: right; white-space: nowrap; }
  .snacks .item { width: 692px; }
  .sides .item { width: 692px; }
  .sides .leader { margin-right: 0; }
  .sides .price { width: 34px; }
  .sides .price.large { width: 71px; }
  .size-heads {
    position: absolute; left: 602px; top: 667px;
    display: flex; font-weight: 700; font-size: 20px; color: var(--ink-blue);
  }
  .size-heads span { text-align: right; }
  .size-heads .sm { width: 40px; }
  .size-heads .lg { width: 71px; }
</style>
</head>
<body>
  <div class="wood-backdrop" role="img" aria-label="Weathered timber plank background"></div>

  <header class="brand-panel">
    <h1 class="brand-name">Copperfinch</h1>
  </header>

  <main class="menu-panel">
    <h2 class="section-title" style="top:0;">Snacks</h2>
    <svg class="section-rule" style="top:68px;" viewBox="0 0 776 24" aria-hidden="true">
      <line x1="0" y1="12" x2="764" y2="12" stroke="var(--wine)" stroke-width="3"/>
      <circle cx="764" cy="12" r="11" fill="var(--ink-blue)"/>
    </svg>
    <ul class="item-list snacks" style="top:97px;">
      <li class="item"><span class="item-name">Pork crackling</span><span class="leader"></span><span class="price">$5</span></li>
      <li class="item"><span class="item-name">Venison pasties &amp; plum sauce</span><span class="leader"></span><span class="price">$12</span></li>
      <li class="item"><span class="item-name">Lamb Meat balls &amp; pomegranate molasses</span><span class="leader"></span><span class="price">$15</span></li>
      <li class="item"><span class="item-name">Pulled pork &amp; apple slaw Sliders</span><span class="leader"></span><span class="price">$12</span></li>
      <li class="item"><span class="item-name">Cheese fondue &amp; Asparagus</span><span class="leader"></span><span class="price">$10</span></li>
      <li class="item"><span class="item-name">Battered fish fingers &amp; tartare sauce</span><span class="leader"></span><span class="price">$9</span></li>
      <li class="item"><span class="item-name">Hand cut fries &amp; tomato sauce</span><span class="leader"></span><span class="price">$7</span></li>
      <li class="item"><span class="item-name">Salmon &amp; avocado filled Sesame cones</span><span class="leader"></span><span class="price">$12</span></li>
      <li class="item"><span class="item-name">Parmesan, chilli &amp; lemon Skinny fries</span><span class="leader"></span><span class="price">$7</span></li>
      <li class="item"><span class="item-name">Barbequed Chicken tulips</span><span class="leader"></span><span class="price">$14</span></li>
      <li class="item"><span class="item-name">Steamed mussels &amp; tomato salsa</span><span class="leader"></span><span class="price">$12</span></li>
      <li class="item"><span class="item-name">Garlic bread</span><span class="leader"></span><span class="price">$6</span></li>
      <li class="item"><span class="item-name">Crispy lentil balls &amp; roast garlic yoghurt</span><span class="leader"></span><span class="price">$8</span></li>
    </ul>

    <h2 class="section-title" style="top:566px;">Salads &amp; sides</h2>
    <svg class="section-rule" style="top:631px;" viewBox="0 0 776 24" aria-hidden="true">
      <line x1="0" y1="12" x2="764" y2="12" stroke="var(--wine)" stroke-width="3"/>
      <circle cx="764" cy="12" r="11" fill="var(--ink-blue)"/>
    </svg>
    <div class="size-heads"><span class="sm">SM</span><span class="lg">LG</span></div>
    <ul class="item-list sides" style="top:689px;">
      <li class="item"><span class="item-name">Warmed Red skinned potatoes with dill &amp; mustard</span><span class="leader"></span><span class="price">$6</span><span class="price large">$9</span></li>
      <li class="item"><span class="item-name">Tomato &amp; mixed beans</span><span class="leader"></span><span class="price">$8</span><span class="price large">$11</span></li>
      <li class="item"><span class="item-name">Char grilled vegetables &amp; halloumi</span><span class="leader"></span><span class="price">$7</span><span class="price large">$10</span></li>
      <li class="item"><span class="item-name">Orzo, broadbean &amp;feta</span><span class="leader"></span><span class="price">$7</span><span class="price large">$10</span></li>
      <li class="item"><span class="item-name">Beetroot, spinach &amp; goats cheese with maple</span><span class="leader"></span><span class="price">$8</span><span class="price large">$11</span></li>
      <li class="item"><span class="item-name">Mixed leaves &amp; citrus emulsion</span><span class="leader"></span><span class="price">$6</span><span class="price large">$9</span></li>
      <li class="item"><span class="item-name">Steamed Broccoli &amp; sesame butter</span><span class="leader"></span><span class="price">$6</span><span class="price large">$9</span></li>
    </ul>
  </main>
</body>
</html>
```